Etiketten für Kräuterbutter Spezialitäten
Zielgruppe
Manufaktur für Kräuterbutter und Grillsaucen Spezialitäten.
Zu unseren Kunden gehören vorwiegend Privatkundschaft, welche den Genuss und vorallem die Freude am grillieren zelebrieren. Natürlich lässt sich unsere Kräuterbutter auch für spannende Pastegerichte oder andere raffinierte Gerichte verwenden.
Aufgabenstellung
- edles Designen das den Charakter der Manufaktur-Produktion rüber bringt
darf vielleicht etwas rustikal sein mit Holz oder etwas das Lust auf grillieren macht.
Vielleicht passt auch der Schiefertafelstil mit Handlettering.
- Logo Layout muss dem entsprechen wie bei allen anderen Kräuterbutter-Spezialitäten von uns.
Wir brauchen:
- Universelles Etikett für verschiedene Kräuterbutter-Spezialitäten einsetzbar
Titel: Kräuterbutter
Grösse 10cm breit x 4.5 cm hoch
Grösse 4.5 cm breit x 4.5 cm hoch
- Universelles Etikett für verschiedene Kräuterschaum-Spezialitäten. (Mit Margarine statt Butter)
Titel: Kräuterschaum
- und dementsprechen ein neutrales Logo-Etikett für einzelprodukte, welche weder mit Butter noch mit Margarine zu tun haben. (kann z.b. Eine Gewürzmischung, ein Geschenkkorb, oder eine Grillsauce sein)
Alle Lebensmittelrechtlichen relevanten Angaben sind auf dem Rücketikett.
Hier brauchen wir nur ein reines Werbeetikett für die Frontseite.

```html
<!DOCTYPE html>
<html lang="de">
<head>
<meta charset="utf-8">
<title>Etiketten Kräuterbutter &amp; Kräuterschaum</title>
<link href="https://fonts.googleapis.com/css2?family=Comfortaa:wght@700&family=Kaushan+Script&display=swap" rel="stylesheet">
<style>
  :root{
    --frame-red:#d7141c;
    --deep-red:#b80f16;
    --slate:#2f3035;
    --slate-light:#45464c;
    --white:#ffffff;
    --line-dark:#3a3a3f;
    --herb-green:#4f8a3a;
    --herb-dark:#2e5a2a;
    --badge-grey:#8d8e92;
  }
  *{box-sizing:border-box;margin:0;padding:0}
  html,body{width:1200px;height:1175px;overflow:hidden;background:var(--white)}
  .sheet{position:relative;width:1200px;height:1175px}
  .label{position:absolute;width:530px;height:238px;border-radius:16px;background:var(--frame-red);padding:7px}
  .label--butter{left:35px}
  .label--schaum{left:651px}
  .row-1{top:27px}.row-2{top:329px}.row-3{top:631px}.row-4{top:933px}
  .slate{position:relative;width:100%;height:100%;border-radius:10px;overflow:hidden;
    background:linear-gradient(170deg,var(--slate-light) 0%,var(--slate) 45%,#26272b 100%)}
  .crown{position:absolute;left:0;top:0;width:516px;height:80px}
  .brand{position:absolute;left:0;right:0;top:14px;text-align:center;
    font-family:"Comfortaa",sans-serif;font-weight:700;font-size:32px;letter-spacing:1px}
  .crown--red + .brand{color:var(--white)}
  .crown--white + .brand{color:var(--frame-red)}
  .herbs{position:absolute;left:0;right:0;bottom:0;height:100px;
    background:linear-gradient(180deg,rgba(79,138,58,0) 0%,rgba(79,138,58,.75) 45%,var(--herb-dark) 100%)}
  .title{position:absolute;left:0;right:0;top:72px;text-align:center;color:var(--white);
    font-family:"Kaushan Script",cursive;font-size:70px;line-height:1}
  .badge{position:absolute;left:231px;top:160px;width:62px;height:72px}
  .tagline{position:absolute;left:300px;top:170px;width:212px;height:46px;
    background:var(--frame-red);transform:rotate(-12deg);
    color:var(--white);font-family:"Kaushan Script",cursive;font-size:28px;line-height:46px;text-align:center}
</style>
</head>
<body>
<main class="sheet">

  <!-- Kräuterbutter, red crown -->
  <section class="label label--butter row-1">
    <div class="slate">
      <div class="herbs" role="img" aria-label="Illustrierte Kräuter: Salbei, Dill, Petersilie, Basilikum"></div>
      <svg class="crown crown--red" viewBox="0 0 516 80"><path d="M55 0 Q258 140 461 0Z" fill="var(--frame-red)"/><path d="M70 0 Q258 124 446 0" fill="none" stroke="var(--deep-red)" stroke-width="3"/></svg>
      <div class="brand">hollmark's</div>
      <h1 class="title">Kräuterbutter</h1>
      <svg class="badge" viewBox="0 0 62 72"><rect x="22" y="44" width="18" height="26" fill="var(--frame-red)"/><circle cx="31" cy="31" r="30" fill="var(--badge-grey)"/></svg>
    </div>
  </section>

  <!-- Kräuterschaum, red crown -->
  <section class="label label--schaum row-1">
    <div class="slate">
      <div class="herbs" role="img" aria-label="Illustrierte Kräuter: Salbei, Dill, Petersilie"></div>
      <svg class="crown crown--red" viewBox="0 0 516 80"><path d="M55 0 Q258 140 461 0Z" fill="var(--frame-red)"/><path d="M70 0 Q258 124 446 0" fill="none" stroke="var(--deep-red)" stroke-width="3"/></svg>
      <div class="brand">hollmark's</div>
      <h1 class="title">Kräuterschaum</h1>
      <svg class="badge" viewBox="0 0 62 72"><rect x="22" y="44" width="18" height="26" fill="var(--frame-red)"/><circle cx="31" cy="31" r="30" fill="var(--badge-grey)"/></svg>
      <div class="tagline">mit Magarine</div>
    </div>
  </section>

  <!-- Kräuterbutter, red crown with white line -->
  <section class="label label--butter row-2">
    <div class="slate">
      <div class="herbs" role="img" aria-label="Illustrierte Kräuter: Salbei, Dill, Petersilie, Basilikum"></div>
      <svg class="crown crown--red" viewBox="0 0 516 80"><path d="M55 0 Q258 140 461 0Z" fill="var(--frame-red)"/><path d="M72 0 Q258 122 444 0" fill="none" stroke="var(--white)" stroke-width="2"/></svg>
      <div class="brand">hollmark's</div>
      <h1 class="title">Kräuterbutter</h1>
      <svg class="badge" viewBox="0 0 62 72"><rect x="22" y="44" width="18" height="26" fill="var(--frame-red)"/><circle cx="31" cy="31" r="30" fill="var(--badge-grey)"/></svg>
    </div>
  </section>

  <!-- Kräuterschaum, red crown with white line -->
  <section class="label label--schaum row-2">
    <div class="slate">
      <div class="herbs" role="img" aria-label="Illustrierte Kräuter: Salbei, Dill, Petersilie"></div>
      <svg class="crown crown--red" viewBox="0 0 516 80"><path d="M55 0 Q258 140 461 0Z" fill="var(--frame-red)"/><path d="M72 0 Q258 122 444 0" fill="none" stroke="var(--white)" stroke-width="2"/></svg>
      <div class="brand">hollmark's</div>
      <h1 class="title">Kräuterschaum</h1>
      <svg class="badge" viewBox="0 0 62 72"><rect x="22" y="44" width="18" height="26" fill="var(--frame-red)"/><circle cx="31" cy="31" r="30" fill="var(--badge-grey)"/></svg>
      <div class="tagline">mit Magarine</div>
    </div>
  </section>

  <!-- Kräuterbutter, white crown with dark line -->
  <section class="label label--butter row-3">
    <div class="slate">
      <div class="herbs" role="img" aria-label="Illustrierte Kräuter: Salbei, Dill, Petersilie, Basilikum"></div>
      <svg class="crown crown--white" viewBox="0 0 516 80"><path d="M55 0 Q258 140 461 0Z" fill="var(--white)"/><path d="M55 0 Q258 140 461 0" fill="none" stroke="var(--line-dark)" stroke-width="4"/></svg>
      <div class="brand">hollmark's</div>
      <h1 class="title">Kräuterbutter</h1>
      <svg class="badge" viewBox="0 0 62 72"><rect x="22" y="44" width="18" height="26" fill="var(--frame-red)"/><circle cx="31" cy="31" r="30" fill="var(--badge-grey)"/></svg>
    </div>
  </section>

  <!-- Kräuterschaum, white crown with dashed line -->
  <section class="label label--schaum row-3">
    <div class="slate">
      <div class="herbs" role="img" aria-label="Illustrierte Kräuter: Salbei, Dill, Petersilie"></div>
      <svg class="crown crown--white" viewBox="0 0 516 80"><path d="M55 0 Q258 140 461 0Z" fill="var(--white)"/><path d="M62 0 Q258 128 454 0" fill="none" stroke="var(--frame-red)" stroke-width="1.5" stroke-dasharray="5 4"/></svg>
      <div class="brand">hollmark's</div>
      <h1 class="title">Kräuterschaum</h1>
      <svg class="badge" viewBox="0 0 62 72"><rect x="22" y="44" width="18" height="26" fill="var(--frame-red)"/><circle cx="31" cy="31" r="30" fill="var(--badge-grey)"/></svg>
      <div class="tagline">mit Magarine</div>
    </div>
  </section>

  <!-- Kräuterbutter, white crown with dashed line -->
  <section class="label label--butter row-4">
    <div class="slate">
      <div class="herbs" role="img" aria-label="Illustrierte Kräuter: Salbei, Dill, Petersilie, Basilikum"></div>
      <svg class="crown crown--white" viewBox="0 0 516 80"><path d="M55 0 Q258 140 461 0Z" fill="var(--white)"/><path d="M62 0 Q258 128 454 0" fill="none" stroke="var(--frame-red)" stroke-width="1.5" stroke-dasharray="5 4"/></svg>
      <div class="brand">hollmark's</div>
      <h1 class="title">Kräuterbutter</h1>
      <svg class="badge" viewBox="0 0 62 72"><rect x="22" y="44" width="18" height="26" fill="var(--frame-red)"/><circle cx="31" cy="31" r="30" fill="var(--badge-grey)"/></svg>
    </div>
  </section>

  <!-- Kräuterschaum, white crown with dark line -->
  <section class="label label--schaum row-4">
    <div class="slate">
      <div class="herbs" role="img" aria-label="Illustrierte Kräuter: Salbei, Dill, Petersilie"></div>
      <svg class="crown crown--white" viewBox="0 0 516 80"><path d="M55 0 Q258 140 461 0Z" fill="var(--white)"/><path d="M55 0 Q258 140 461 0" fill="none" stroke="var(--line-dark)" stroke-width="4"/></svg>
      <div class="brand">hollmark's</div>
      <h1 class="title">Kräuterschaum</h1>
      <svg class="badge" viewBox="0 0 62 72"><rect x="22" y="44" width="18" height="26" fill="var(--frame-red)"/><circle cx="31" cy="31" r="30" fill="var(--badge-grey)"/></svg>
      <div class="tagline">mit Magarine</div>
    </div>
  </section>

</main>
</body>
</html>
```